Wordpress website design for membership site

I need a wordpress website designed for a membership site specializing in member video recordings and storage. I need the site to be simplistic but fully functional. I want a minimalistic landing and member page. The member page needs to be able to showcase the members recorded videos amd utilize a GUI system of navigation utilizing graphical buttons. Member signup page needs to be fully functional to include email verification and password change/recovery functionality.

Coding

Coded - Design and coding required

Number of Pages Required

3 page

Font styles to use
Sans Serif

Colors

Designer to choose colors to be used in the design.

Requirements
Must have
• The project must incorporate the name ZELQON or ZELQON.com within the design.
Should not have
• Project should not use prepublished templates available online but should be unique in design and functionality.

```html
<!DOCTYPE html>
<html lang="en">
<head>
<meta charset="utf-8">
<title>ZELQON – Best Online Storage for Videos</title>
<link href="https://fonts.googleapis.com/css2?family=Montserrat:wght@400;500;600;700&family=Mulish:wght@400;600;700&display=swap" rel="stylesheet">
<style>
:root{
  --violet:#2a0c66;
  --violet-deep:#1e0850;
  --violet-btn:#3b1a80;
  --ink:#1b1b1b;
  --grey:#666666;
  --grey-card:#6b6b6b;
  --white:#ffffff;
  --line:#e2e2e2;
  --footer:#1c1c22;
}
*{box-sizing:border-box;margin:0;padding:0}
html,body{width:1200px;height:3340px;overflow:hidden}
body{position:relative;background:var(--white);font-family:'Mulish',Arial,sans-serif;color:var(--ink)}
.abs{position:absolute}
.center{text-align:center}
/* top bar */
.topbar{left:0;top:0;width:1200px;height:40px;background:var(--violet-deep);color:var(--white);font-size:15px;font-family:'Montserrat',Arial,sans-serif}
.topbar .call{left:92px;top:0;height:40px;line-height:40px;padding:0 14px;border-left:1px solid rgba(255,255,255,.2);border-right:1px solid rgba(255,255,255,.2);display:flex;align-items:center;gap:6px}
.topbar .addr{right:92px;top:0;height:40px;line-height:40px;padding:0 14px;border-left:1px solid rgba(255,255,255,.2);border-right:1px solid rgba(255,255,255,.2);display:flex;align-items:center;gap:6px;font-size:14px}
/* header */
.header{left:0;top:40px;width:1200px;height:112px;background:var(--white)}
.brand{left:95px;top:20px;width:310px;text-align:center;color:var(--violet)}
.brand-name{font-family:'Montserrat',Arial,sans-serif;font-weight:700;font-size:34px;letter-spacing:1px;line-height:40px}
.brand-tag{font-family:'Montserrat',Arial,sans-serif;font-weight:500;font-size:16px;margin-top:4px}
.nav{left:464px;top:44px;display:flex;gap:0;font-family:'Montserrat',Arial,sans-serif;font-size:16px;color:var(--ink)}
.nav span{margin-right:44px}
.nav .active{color:var(--violet);font-weight:600}
/* hero */
.hero{left:0;top:152px;width:1200px;height:606px;clip-path:polygon(0 0,100% 0,100% 85%,0 100%);
  background:radial-gradient(ellipse at 50% 45%,#5a5a7c 0%,#2c2a44 45%,#141424 100%)}
.hero-title{left:0;top:316px;width:1200px;color:var(--white);font-family:'Montserrat',Arial,sans-serif;font-weight:700;font-size:52px;letter-spacing:1px}
.hero-sub{left:0;top:395px;width:1200px;color:var(--white);font-family:'Montserrat',Arial,sans-serif;font-weight:700;font-size:33px}
.hero-btn{left:432px;top:464px;width:336px;height:66px;background:var(--violet-btn);color:var(--white);border-radius:4px;font-family:'Montserrat',Arial,sans-serif;font-weight:600;font-size:25px;display:flex;align-items:center;justify-content:center;gap:16px}
/* process */
.section-title{left:0;width:1200px;color:var(--violet);font-family:'Montserrat',Arial,sans-serif;font-weight:700;text-align:center}
.step-circle{width:148px;height:148px;border-radius:50%;display:flex;align-items:center;justify-content:center}
.step-circle.violet{background:var(--violet)}
.step-circle.grey{background:var(--grey)}
.step-label{width:320px;text-align:center;font-family:'Montserrat',Arial,sans-serif;font-weight:700;font-size:22px}
.step-text{width:320px;text-align:center;font-size:16px;line-height:31px;color:var(--ink)}
/* about */
.about{left:0;top:1343px;width:1200px;height:707px;clip-path:polygon(0 13%,100% 0,100% 100%,0 89%);
  background:radial-gradient(ellipse at 50% 40%,#3c1d84 0%,#2a0c66 55%,#1d0748 100%)}
.about-title{left:0;top:1503px;width:1200px;color:var(--white);font-family:'Montserrat',Arial,sans-serif;font-weight:700;font-size:36px}
.about-sub{left:0;top:1552px;width:1200px;color:var(--white);font-family:'Montserrat',Arial,sans-serif;font-weight:600;font-size:27px}
.about-text{left:162px;top:1601px;width:876px;color:var(--white);font-size:18px;line-height:31.5px;text-align:justify;text-align-last:center}
.outline-btn{left:512px;top:1840px;width:176px;height:46px;border:2px solid var(--white);color:var(--white);font-family:'Montserrat',Arial,sans-serif;font-weight:600;font-size:16px;display:flex;align-items:center;justify-content:center}
/* pricing */
.plan{background:var(--white);border:1px solid var(--line);overflow:hidden}
.plan-head{position:relative;height:90px}
.plan-head svg{position:absolute;left:0;top:0}
.plan-name{position:absolute;left:0;top:24px;width:100%;text-align:center;color:var(--white);font-family:'Montserrat',Arial,sans-serif;font-weight:700;font-size:20px}
.price{text-align:center;color:var(--grey);font-family:'Montserrat',Arial,sans-serif;font-weight:700;font-size:27px;margin-top:6px}
.per{text-align:center;color:var(--grey);font-family:'Montserrat',Arial,sans-serif;font-weight:600;font-size:16px;margin-top:2px}
.features{list-style:none;margin:22px 0 0 44px}
.features li{display:flex;align-items:center;gap:14px;font-size:13px;color:#333;height:27px}
.plan-note{text-align:center;font-size:16px;line-height:21px;color:#333;margin-top:20px}
.plan-btn{margin:22px auto 0;width:142px;height:40px;background:var(--violet-btn);color:var(--white);font-family:'Montserrat',Arial,sans-serif;font-weight:600;font-size:13px;display:flex;align-items:center;justify-content:center}
.plan.featured{box-shadow:0 2px 10px rgba(0,0,0,.12)}
.plan.featured .price,.plan.featured .per{color:var(--violet)}
/* footer */
.footer{left:0;top:2795px;width:1200px;height:545px;clip-path:polygon(0 0,100% 16%,100% 100%,0 100%);
  background:radial-gradient(ellipse at 60% 30%,#3a2c38 0%,#232029 45%,#141418 100%)}
.foot-icon{width:82px;height:82px;border:2px solid var(--white);border-radius:50%;display:flex;align-items:center;justify-content:center}
.foot-text{width:300px;text-align:center;color:var(--white);font-size:17px;line-height:31px}
.foot-nav{left:0;top:3170px;width:1200px;display:flex;justify-content:center;color:var(--white);font-size:17px}
.foot-nav span.sep{margin:0 12px;opacity:.8}
.copy{left:0;top:3218px;width:1200px;text-align:center;color:#bfbfbf;font-size:15px}
.social{left:528px;top:3258px;display:flex;gap:8px}
.social span{width:32px;height:32px;border:2px solid var(--white);border-radius:50%}
</style>
</head>
<body>

<!-- top bar -->
<div class="abs topbar">
  <div class="abs call">
    <svg width="15" height="15" viewBox="0 0 24 24"><path fill="#fff" d="M6.6 10.8a15 15 0 0 0 6.6 6.6l2.2-2.2c.3-.3.7-.4 1-.2 1.1.4 2.3.6 3.6.6.6 0 1 .4 1 1V20c0 .6-.4 1-1 1A17 17 0 0 1 3 4c0-.6.4-1 1-1h3.5c.6 0 1 .4 1 1 0 1.3.2 2.5.6 3.6.1.3 0 .7-.2 1z"/></svg>
    Call us: (555) 013-4826
  </div>
  <div class="abs addr">
    <svg width="13" height="16" viewBox="0 0 24 30"><path fill="#fff" d="M12 0a10 10 0 0 0-10 10c0 7.5 10 20 10 20s10-12.5 10-20A10 10 0 0 0 12 0zm0 14a4 4 0 1 1 0-8 4 4 0 0 1 0 8z"/></svg>
    480 Lumen Park Way Brightvale, CA 90377
  </div>
</div>

<!-- header -->
<header class="abs header">
  <div class="abs brand">
    <div class="brand-name">ZELQON</div>
    <div class="brand-tag">Preserving You For Future Generations</div>
  </div>
  <nav class="abs nav">
    <span class="active">Home</span><span>About</span><span>Gallery</span><span>Join Us</span><span>Blogs</span><span>Faq</span><span>Profile</span><span>Contact</span>
  </nav>
</header>

<!-- hero -->
<div class="abs hero" role="img" aria-label="Hands holding a tablet over a wall of video thumbnails"></div>
<h1 class="abs hero-title center">WELCOME TO ZELQON</h1>
<h2 class="abs hero-sub center">BEST ONLINE STORAGE FOR VIDEOS 2019</h2>
<div class="abs hero-btn">
  <svg width="26" height="24" viewBox="0 0 24 22"><path fill="#fff" d="M23 0 0 10l7 3 12-9-9 11v7l4-5 5 3z"/></svg>
  GET A MEMBERSHIP
</div>

<!-- process -->
<h2 class="abs section-title" style="top:862px;font-size:32px">PROCESS</h2>
<svg class="abs" style="left:334px;top:966px" width="200" height="50" viewBox="0 0 200 50">
  <path d="M0 30 Q100 -10 200 35" fill="none" stroke="#2a0c66" stroke-width="2" stroke-dasharray="4 4"/>
  <path d="M90 4 l8 6 -8 6" fill="none" stroke="#2a0c66" stroke-width="2.5"/>
</svg>
<svg class="abs" style="left:674px;top:1000px" width="200" height="60" viewBox="0 0 200 60">
  <path d="M0 15 Q100 70 200 25" fill="none" stroke="#2a0c66" stroke-width="2" stroke-dasharray="4 4"/>
  <path d="M92 30 l8 7 -8 7" fill="none" stroke="#2a0c66" stroke-width="2.5"/>
</svg>

<div class="abs step-circle violet" style="left:186px;top:943px">
  <svg width="86" height="66" viewBox="0 0 86 66" fill="none" stroke="#fff" stroke-width="3">
    <rect x="3" y="14" width="80" height="48" rx="3"/><rect x="34" y="3" width="18" height="14" rx="2"/>
    <circle cx="24" cy="32" r="6"/><path d="M14 48c2-6 18-6 20 0"/>
    <path d="M44 30h28M44 38h28M44 46h18"/>
  </svg>
</div>
<div class="abs step-circle grey" style="left:526px;top:943px">
  <svg width="76" height="76" viewBox="0 0 76 76" fill="#fff">
    <path d="M38 6 18 28h12v18h16V28h12z"/><rect x="8" y="52" width="60" height="16" rx="3"/>
    <circle cx="56" cy="60" r="2.5" fill="#666"/><circle cx="48" cy="60" r="2.5" fill="#666"/>
  </svg>
</div>
<div class="abs step-circle violet" style="left:864px;top:943px">
  <svg width="74" height="84" viewBox="0 0 74 84" fill="none" stroke="#fff" stroke-width="3.5">
    <path d="M37 4 6 14v24c0 20 14 34 31 42 17-8 31-22 31-42V14z"/>
    <circle cx="37" cy="42" r="15"/><path d="M30 42l5 5 10-10"/>
  </svg>
</div>

<div class="abs step-label" style="left:100px;top:1110px;color:var(--violet)">GET MEMBERSHIP</div>
<div class="abs step-label" style="left:440px;top:1110px;color:var(--grey)">UNLIMITED UPLOADS</div>
<div class="abs step-label" style="left:778px;top:1110px;color:var(--violet)">SECURE VIDEOS</div>
<p class="abs step-text" style="left:100px;top:1150px">Sed ut perspiciatis unde omnis iste natus error sit voluptatem accutium doloremque</p>
<p class="abs step-text" style="left:440px;top:1150px">Sed ut perspiciatis unde omnis iste natus error sit voluptatem accutium doloremque</p>
<p class="abs step-text" style="left:778px;top:1150px">Sed ut perspiciatis unde omnis iste natus error sit voluptatem accutium doloremque</p>

<!-- about -->
<div class="abs about" role="img" aria-label="Hand holding a phone in front of a wall of video screens, violet tint"></div>
<h2 class="abs about-title center">ABOUT ZELQON</h2>
<h3 class="abs about-sub center">Preserving you for future generations</h3>
<p class="abs about-text">Sed ut perspiciatis unde omnis iste natus error sit voluptatem accusantium doloremque laudantium, totam rem aperiam, eaque ipsa quae ab illo inventore veritatis et quasi architecto beatae vitae dicta sunt explicabo. Nemo enim ipsam voluptatem quia voluptas sit aspernatur aut odit aut fugit, sed quia consequuntur magni dolores eos qui ratione voluptatem sequi nesciunt. Neque porro quisquam est, qui dolorem ipsum quia dolor sit amet, consectetur, adipisci velit, sed quia non numquam eius modi tempora incidunt ut labore et dolore magnam aliquam quaerat voluptatem.</p>
<div class="abs outline-btn">READ MORE</div>

<!-- pricing -->
<h2 class="abs section-title" style="top:2154px;font-size:35px">BEST ONLINE STORAGE FOR VIDEOS 2019</h2>

<div class="abs plan" style="left:212px;top:2254px;width:248px;height:414px">
  <div class="plan-head">
    <svg width="248" height="90" viewBox="0 0 248 90"><path d="M0 0h248v80c-40-22-80 14-124 0S40 58 0 80z" fill="#6b6b6b"/></svg>
    <div class="plan-name" style="top:26px">SILVER</div>
  </div>
  <div class="price">$.02</div>
  <div class="per">(per space)</div>
  <ul class="features" style="margin-left:40px;margin-top:14px">
    <li><svg width="13" height="13" viewBox="0 0 14 14"><rect x="1" y="2" width="11" height="11" fill="none" stroke="#2a0c66" stroke-width="1.6"/><path d="M4 7l3 3 6-8" fill="none" stroke="#2a0c66" stroke-width="2"/></svg>Sync Folder</li>
    <li><svg width="13" height="13" viewBox="0 0 14 14"><rect x="1" y="2" width="11" height="11" fill="none" stroke="#2a0c66" stroke-width="1.6"/><path d="M4 7l3 3 6-8" fill="none" stroke="#2a0c66" stroke-width="2"/></svg>File Link Sharing</li>
    <li><svg width="13" height="13" viewBox="0 0 14 14"><rect x="1" y="2" width="11" height="11" fill="none" stroke="#2a0c66" stroke-width="1.6"/><path d="M4 7l3 3 6-8" fill="none" stroke="#2a0c66" stroke-width="2"/></svg>Folder Sharing</li>
    <li><svg width="13" height="13" viewBox="0 0 14 14"><rect x="1" y="2" width="11" height="11" fill="none" stroke="#2a0c66" stroke-width="1.6"/><path d="M4 7l3 3 6-8" fill="none" stroke="#2a0c66" stroke-width="2"/></svg>Versioning</li>
  </ul>
  <p class="plan-note">Lorem ipsum dolor<br>consectetur adipiscing</p>
  <div class="plan-btn" style="margin-top:14px">READ MORE</div>
</div>

<div class="abs plan featured" style="left:459px;top:2238px;width:278px;height:448px">
  <div class="plan-head" style="height:98px">
    <svg width="278" height="98" viewBox="0 0 278 98"><path d="M0 0h278v88c-46-24-90 16-139 0S46 64 0 88z" fill="#2a0c66"/></svg>
    <div class="plan-name" style="top:24px">GOLD</div>
  </div>
  <div class="price" style="margin-top:0">$.04</div>
  <div class="per">(per space)</div>
  <ul class="features" style="margin-left:40px;margin-top:14px">
    <li><svg width="13" height="13" viewBox="0 0 14 14"><rect x="1" y="2" width="11" height="11" fill="none" stroke="#2a0c66" stroke-width="1.6"/><path d="M4 7l3 3 6-8" fill="none" stroke="#2a0c66" stroke-width="2"/></svg>Sync Folder</li>
    <li><svg width="13" height="13" viewBox="0 0 14 14"><rect x="1" y="2" width="11" height="11" fill="none" stroke="#2a0c66" stroke-width="1.6"/><path d="M4 7l3 3 6-8" fill="none" stroke="#2a0c66" stroke-width="2"/></svg>File Link Sharing</li>
    <li><svg width="13" height="13" viewBox="0 0 14 14"><rect x="1" y="2" width="11" height="11" fill="none" stroke="#2a0c66" stroke-width="1.6"/><path d="M4 7l3 3 6-8" fill="none" stroke="#2a0c66" stroke-width="2"/></svg>Folder Sharing</li>
    <li><svg width="13" height="13" viewBox="0 0 14 14"><rect x="1" y="2" width="11" height="11" fill="none" stroke="#2a0c66" stroke-width="1.6"/><path d="M4 7l3 3 6-8" fill="none" stroke="#2a0c66" stroke-width="2"/></svg>Versioning</li>
    <li><svg width="13" height="13" viewBox="0 0 14 14"><rect x="1" y="2" width="11" height="11" fill="none" stroke="#2a0c66" stroke-width="1.6"/><path d="M4 7l3 3 6-8" fill="none" stroke="#2a0c66" stroke-width="2"/></svg>Organization and content</li>
    <li><svg width="13" height="13" viewBox="0 0 14 14"><rect x="1" y="2" width="11" height="11" fill="none" stroke="#2a0c66" stroke-width="1.6"/><path d="M4 7l3 3 6-8" fill="none" stroke="#2a0c66" stroke-width="2"/></svg>Plot and pacing</li>
    <li><svg width="13" height="13" viewBox="0 0 14 14"><rect x="1" y="2" width="11" height="11" fill="none" stroke="#2a0c66" stroke-width="1.6"/><path d="M4 7l3 3 6-8" fill="none" stroke="#2a0c66" stroke-width="2"/></svg>Manuscript Review</li>
  </ul>
  <div class="plan-btn" style="margin-top:20px">READ MORE</div>
</div>

<div class="abs plan" style="left:737px;top:2254px;width:252px;height:414px">
  <div class="plan-head" style="height:84px">
    <svg width="252" height="84" viewBox="0 0 252 84"><path d="M0 0h252v74c-40-22-82 14-126 0S40 52 0 74z" fill="#6b6b6b"/></svg>
    <div class="plan-name" style="top:24px">PLATINUM</div>
  </div>
  <div class="price" style="margin-top:0">$.06</div>
  <div class="per">(per space)</div>
  <ul class="features" style="margin-left:34px;margin-top:10px">
    <li><svg width="13" height="13" viewBox="0 0 14 14"><rect x="1" y="2" width="11" height="11" fill="none" stroke="#2a0c66" stroke-width="1.6"/><path d="M4 7l3 3 6-8" fill="none" stroke="#2a0c66" stroke-width="2"/></svg>Sync Folder</li>
    <li><svg width="13" height="13" viewBox="0 0 14 14"><rect x="1" y="2" width="11" height="11" fill="none" stroke="#2a0c66" stroke-width="1.6"/><path d="M4 7l3 3 6-8" fill="none" stroke="#2a0c66" stroke-width="2"/></svg>File Link Sharing</li>
    <li><svg width="13" height="13" viewBox="0 0 14 14"><rect x="1" y="2" width="11" height="11" fill="none" stroke="#2a0c66" stroke-width="1.6"/><path d="M4 7l3 3 6-8" fill="none" stroke="#2a0c66" stroke-width="2"/></svg>Folder Sharing</li>
    <li><svg width="13" height="13" viewBox="0 0 14 14"><rect x="1" y="2" width="11" height="11" fill="none" stroke="#2a0c66" stroke-width="1.6"/><path d="M4 7l3 3 6-8" fill="none" stroke="#2a0c66" stroke-width="2"/></svg>Versioning</li>
    <li><svg width="13" height="13" viewBox="0 0 14 14"><rect x="1" y="2" width="11" height="11" fill="none" stroke="#2a0c66" stroke-width="1.6"/><path d="M4 7l3 3 6-8" fill="none" stroke="#2a0c66" stroke-width="2"/></svg>Organization and content</li>
    <li><svg width="13" height="13" viewBox="0 0 14 14"><rect x="1" y="2" width="11" height="11" fill="none" stroke="#2a0c66" stroke-width="1.6"/><path d="M4 7l3 3 6-8" fill="none" stroke="#2a0c66" stroke-width="2"/></svg>Pre-publication proofread</li>
    <li><svg width="13" height="13" viewBox="0 0 14 14"><rect x="1" y="2" width="11" height="11" fill="none" stroke="#2a0c66" stroke-width="1.6"/><path d="M4 7l3 3 6-8" fill="none" stroke="#2a0c66" stroke-width="2"/></svg>Formatting (print and ebook)</li>
  </ul>
  <div class="plan-btn" style="margin-top:16px">READ MORE</div>
</div>

<!-- footer -->
<div class="abs footer" role="img" aria-label="Dark photo of a laptop with a glowing video play screen"></div>

<div class="abs foot-icon" style="left:262px;top:2994px">
  <svg width="40" height="46" viewBox="0 0 40 46" fill="none" stroke="#fff" stroke-width="2.2"><path d="M20 2a13 13 0 0 0-13 13c0 10 13 24 13 24s13-14 13-24A13 13 0 0 0 20 2z"/><circle cx="20" cy="15" r="5"/><path d="M8 36c-5 1-6 3-6 4 0 2 8 4 18 4s18-2 18-4c0-1-1-3-6-4"/></svg>
</div>
<div class="abs foot-icon" style="left:562px;top:2994px">
  <svg width="40" height="40" viewBox="0 0 24 24" fill="none" stroke="#fff" stroke-width="1.3"><path d="M6.6 10.8a15 15 0 0 0 6.6 6.6l2.2-2.2c.3-.3.7-.4 1-.2 1.1.4 2.3.6 3.6.6.6 0 1 .4 1 1V20c0 .6-.4 1-1 1A17 17 0 0 1 3 4c0-.6.4-1 1-1h3.5c.6 0 1 .4 1 1 0 1.3.2 2.5.6 3.6.1.3 0 .7-.2 1z"/><path d="M14 3a7 7 0 0 1 7 7M14 6.5a3.5 3.5 0 0 1 3.5 3.5"/></svg>
</div>
<div class="abs foot-icon" style="left:867px;top:2994px">
  <svg width="44" height="32" viewBox="0 0 44 32" fill="none" stroke="#fff" stroke-width="2.2"><rect x="2" y="2" width="40" height="28" rx="2"/><path d="M2 4l20 16L42 4M2 30l15-13M42 30 27 17"/></svg>
</div>

<p class="abs foot-text" style="left:153px;top:3086px">480 Lumen Park Way<br>Brightvale, CA 90377</p>
<p class="abs foot-text" style="left:453px;top:3086px">Phone:<br>(555) 013-4826</p>
<p class="abs foot-text" style="left:758px;top:3086px">Email:<br>hello@zelqonmail.com</p>

<nav class="abs foot-nav">
  <span>Home</span><span class="sep">|</span><span>About Us</span><span class="sep">|</span><span>Gallery</span><span class="sep">|</span><span>Join Us</span><span class="sep">|</span><span>Blogs</span><span class="sep">|</span><span>Faq</span><span class="sep">|</span><span>Profile</span><span class="sep">|</span><span>Contact Us</span>
</nav>
<p class="abs copy">© 2019 Company Name&nbsp; All right reserved</p>
<div class="abs social" aria-label="Social links"><span></span><span></span><span></span><span></span></div>

</body>
</html>
```